International oil and gas consultancy needs a business card design

We need a business card design for a new oil and gas consultancy business based in Perth Australia. This is a professional services business and needs a moderately conservative type of business card. The business card also needs to be simple and uncluttered. The colour of the business logo is dark red (see attached file).
The front of the card should have a white background and mainly black lettering and perhaps some use of dark red and/or grey (your choice).
The back of the card should have a light grey background with dark red, black and or both dark red & black lettering (your choice).
Please find attached a clear brief of how I would like the business card designed.
Updates

Hello Everyone, I have slightly modified the brief. The main change is to incorporate some dark red and grey colours into the card, while still keeping the black lettering dominant. I have made the changes in the attached detailed brief document. Regards

Please note, the front of the card must say Harbor Ledger Advisory (in addition to the logo).

Industry/Entity Type

Conservative

Requirements
Must have
• brief has been updated. please refer to attachment for details.

Front of the card MUST say Harbor Ledger Advisory (in addition to the logo)

```html
<!DOCTYPE html>
<html lang="en">
<head>
<meta charset="utf-8">
<title>Harbor Ledger Advisory – Business Card</title>
<link rel="stylesheet" href="https://fonts.googleapis.com/css2?family=Arimo:wght@400;700&display=swap">
<style>
  :root {
    --page: #e9e7e4;
    --card-white: #ffffff;
    --charcoal: #3a3a3c;
    --charcoal-deep: #2a2a2c;
    --brand-red: #8c1c20;
    --band-red: #9a1f24;
    --ink: #2b2b2b;
    --light-text: #f2f2f2;
    --rule: #8a8a8a;
  }
  * { box-sizing: border-box; margin: 0; padding: 0; }
  html, body { width: 1200px; height: 784px; overflow: hidden; }
  body {
    background: var(--page);
    font-family: "Arimo", Arial, sans-serif;
    position: relative;
  }
  .card {
    position: absolute;
    width: 540px;
    height: 330px;
    top: 227px;
    box-shadow: 0 6px 18px rgba(0,0,0,0.18);
    overflow: hidden;
  }

  /* Back of card */
  .card-back {
    left: 40px;
    background: radial-gradient(ellipse at 50% 40%, var(--charcoal) 0%, var(--charcoal-deep) 100%);
  }
  .services {
    position: absolute;
    top: 58px;
    left: 0; right: 0;
    text-align: center;
    list-style: none;
    color: var(--light-text);
    font-size: 15px;
    letter-spacing: 0.32em;
    line-height: 2;
  }
  .specialty {
    position: absolute;
    bottom: 62px;
    left: 0; right: 0;
    text-align: center;
    color: var(--brand-red);
    font-weight: 700;
    font-size: 12.5px;
    letter-spacing: 0.06em;
    text-transform: uppercase;
  }

  /* Front of card */
  .card-front {
    left: 620px;
    background: linear-gradient(180deg, var(--charcoal) 0%, var(--charcoal-deep) 100%);
  }
  .front-header {
    position: absolute;
    top: 0; left: 0; right: 0;
    height: 178px;
    background: var(--card-white);
    text-align: center;
    padding-top: 42px;
  }
  .brand-mark {
    display: inline-flex;
    align-items: center;
    gap: 14px;
    color: var(--brand-red);
    font-weight: 700;
    font-size: 66px;
    line-height: 1;
    letter-spacing: 0.02em;
  }
  .brand-mark .brand-square {
    width: 22px; height: 22px;
    background: var(--brand-red);
  }
  .brand-name {
    margin-top: 8px;
    color: var(--ink);
    font-size: 21px;
  }
  .red-band {
    position: absolute;
    top: 178px; left: 0; right: 0;
    height: 9px;
    background: var(--band-red);
  }
  .person {
    position: absolute;
    top: 214px;
    right: 298px;
    text-align: right;
    color: var(--light-text);
    font-size: 14px;
    line-height: 1.45;
  }
  .person .person-name {
    color: #c23a3e;
    font-size: 20px;
    line-height: 1.2;
  }
  .divider {
    position: absolute;
    top: 206px;
    left: 262px;
    width: 1px;
    height: 100px;
    background: var(--rule);
  }
  .contact {
    position: absolute;
    top: 210px;
    left: 280px;
    display: flex;
    gap: 10px;
    color: var(--light-text);
    font-size: 12.5px;
    line-height: 1.45;
  }
  .contact-icons {
    display: flex;
    flex-direction: column;
    gap: 3px;
    padding-top: 20px;
  }
  .contact-icons svg { width: 13px; height: 13px; fill: var(--band-red); }
  .contact-lines { list-style: none; }
</style>
</head>
<body>

  <section class="card card-back" aria-label="Back of business card">
    <ul class="services">
      <li>JOINT VENTURE AUDITS</li>
      <li>CONTRACT AUDITS</li>
      <li>OPERATIONAL AUDITS</li>
    </ul>
    <p class="specialty">Specialist financial consultants to the oil and gas industry</p>
  </section>

  <section class="card card-front" aria-label="Front of business card">
    <header class="front-header">
      <div class="brand-mark"><span class="brand-square"></span>HLA</div>
      <p class="brand-name">Harbor Ledger Advisory</p>
    </header>
    <div class="red-band"></div>

    <div class="person">
      <p class="person-name">Daniel Marsh</p>
      <p class="person-title">Director</p>
      <p class="person-region">Australasia and South East Asia</p>
    </div>

    <div class="divider"></div>

    <div class="contact">
      <div class="contact-icons">
        <svg viewBox="0 0 24 24" aria-label="Phone"><path d="M6.6 10.8a15 15 0 0 0 6.6 6.6l2.2-2.2c.3-.3.7-.4 1-.2 1.1.4 2.3.6 3.6.6.6 0 1 .4 1 1V20c0 .6-.4 1-1 1A17 17 0 0 1 3 4c0-.6.4-1 1-1h3.5c.6 0 1 .4 1 1 0 1.3.2 2.5.6 3.6.1.3 0 .7-.2 1z"/></svg>
        <svg viewBox="0 0 24 24" aria-label="Email"><path d="M12 2a10 10 0 1 0 4.5 18.9l-.8-1.8A8 8 0 1 1 20 12v1.2a1.7 1.7 0 0 1-3.4 0V7.5h-2v.8A5 5 0 1 0 15.6 16a3.7 3.7 0 0 0 6.4-2.8V12A10 10 0 0 0 12 2zm0 13a3 3 0 1 1 0-6 3 3 0 0 1 0 6z"/></svg>
        <svg viewBox="0 0 24 24" aria-label="Website"><circle cx="12" cy="12" r="9" fill="none" stroke="#9a1f24" stroke-width="2.4"/><path d="M3 12h18M12 3c3 3 3 15 0 18M12 3c-3 3-3 15 0 18" fill="none" stroke="#9a1f24" stroke-width="1.8"/></svg>
      </div>
      <ul class="contact-lines">
        <li>N/A for the business card</li>
        <li>+61 (0)400 555 019</li>
        <li>daniel@harborledger.com</li>
        <li>www.harborledger.com</li>
        <li>ABN: 12 345 678 901</li>
      </ul>
    </div>
  </section>

</body>
</html>
```